New Zealand Luggage Importer Needs Business Cards

We need professional, creative and fashionable business cards created.
We are based in New Zealand and import and distribute high-end, quality, fashionable and durable luggage.
We pride ourselves on selling the very best quality luggage, second only to 1 brand (which we won't mention here)...we use the same manufacturer. However, our prices are much more reasonable.
Industry/Entity Type
Business
Contact Information for Business Card
Mark Dunsley
027 512 4068
3/17 Harlow Street, Pinecrest Flats, Auckland, 0614
PO Box 204377, Fernside, Auckland 0731
09-528-3916
sales@brivancases.co.nz / www.brivancases.co.nz

```html
<!DOCTYPE html>
<html lang="en">
<head>
<meta charset="utf-8">
<title>Brivan Cases – Business Cards</title>
<link href="https://fonts.googleapis.com/css2?family=Open+Sans:wght@400;600;700&display=swap" rel="stylesheet">
<style>
  :root {
    --stage: #202020;
    --card: #ffffff;
    --ink: #1c1a1a;
    --gold: #c9a24a;
    --gold-band: #e5c45a;
    --muted: #444444;
    --rule: #8a8a8a;
  }
  * { box-sizing: border-box; margin: 0; padding: 0; }
  html, body { width: 1200px; height: 1000px; overflow: hidden; }
  body { font-family: "Open Sans", Arial, sans-serif; background: #ffffff; position: relative; }

  .stage { position: absolute; left: 0; top: 0; width: 1200px; height: 780px; background: var(--stage); }

  .card {
    position: absolute; width: 540px; height: 310px; background: var(--card);
    border-radius: 22px; overflow: hidden;
  }
  .card--front { left: 150px; top: 70px; }
  .card--back { left: 510px; top: 410px; }

  .front-brand {
    position: absolute; left: 0; right: 0; top: 105px; text-align: center;
    font-weight: 700; font-size: 46px; letter-spacing: 2px; color: var(--ink);
  }
  .front-web {
    position: absolute; left: 0; right: 0; top: 178px; text-align: center;
    font-size: 13px; letter-spacing: 7px; color: var(--ink);
  }

  .back-brand {
    position: absolute; left: 50px; top: 92px; width: 215px;
    font-weight: 700; font-size: 38px; line-height: 42px; color: var(--ink); text-align: right;
  }
  .back-divider { position: absolute; left: 285px; top: 86px; width: 1px; height: 108px; background: var(--rule); }
  .back-name {
    position: absolute; left: 300px; top: 30px; font-weight: 700; font-size: 28px; color: var(--gold);
    padding-left: 12px; border-left: 3px solid var(--gold); line-height: 30px;
  }
  .contact-list { position: absolute; left: 300px; top: 82px; list-style: none; }
  .contact-list li { display: flex; align-items: center; gap: 10px; font-size: 14px; color: var(--ink); height: 23px; }
  .contact-list svg { width: 12px; height: 12px; fill: var(--gold); }

  .address-band {
    position: absolute; left: 0; right: 0; bottom: 0; height: 88px; background: var(--gold-band);
    border-radius: 40px 0 0 0; padding: 22px 0 0 90px; font-size: 14px; line-height: 20px; color: var(--muted);
  }

  .logo-strip {
    position: absolute; left: 0; top: 780px; width: 1200px; height: 220px;
    display: flex; align-items: center; justify-content: center;
    font-weight: 700; font-size: 92px; letter-spacing: 4px; color: var(--ink);
  }
</style>
</head>
<body>
  <div class="stage">
    <section class="card card--front">
      <div class="front-brand">BRIVAN CASES</div>
      <div class="front-web">www.brivancases.co.nz</div>
    </section>

    <section class="card card--back">
      <div class="back-brand">BRIVAN<br>CASES</div>
      <div class="back-divider"></div>
      <div class="back-name">MARK DUNSLEY</div>
      <ul class="contact-list">
        <li><svg viewBox="0 0 12 12"><path d="M2 1h3l1 3-2 1c.7 1.5 1.5 2.3 3 3l1-2 3 1v3c-5 0-9-4-9-9z"/></svg>027 512 4068</li>
        <li><svg viewBox="0 0 12 12"><path d="M2 1h3l1 3-2 1c.7 1.5 1.5 2.3 3 3l1-2 3 1v3c-5 0-9-4-9-9z"/></svg>09-528-3916</li>
        <li><svg viewBox="0 0 12 12"><path d="M0 2h12v8H0z M0 2l6 4 6-4" stroke="#fff" stroke-width="1"/></svg>sales@brivancases.co.nz</li>
        <li><svg viewBox="0 0 12 12"><circle cx="6" cy="6" r="5.5"/><path d="M0.5 6h11M6 0.5v11" stroke="#fff" stroke-width="0.8"/></svg>www.brivancases.co.nz</li>
      </ul>
      <div class="address-band">
        PO Box 204377, Fernside, Auckland 0731<br>
        3/17 Harlow Street, Pinecrest Flats, Auckland, 0614
      </div>
    </section>
  </div>

  <div class="logo-strip">BRIVAN CASES</div>
</body>
</html>
```